eMail HTML Marketing Template

I need an HTML e-mail marketing template design based off our current website theme (www.tindleport.com). If you need anymore info or have questions please let me know and I will get back to you ASAP.

Goal: A monthly newsletter template for email marketing. Please use lorem ipsum for content filler. If you need to purchase images for the design please let me know and the price to do so.

Thanks.

***URGENT***
If anyone can provide a well designed mockup by 4:00PM EST today (2/6/13) I will award up to two participation prizes of $20 each to each submitter.

Goal: A monthly newsletter template for email marketing.  Please use lorem ipsum for content filler. If you need to purchase images for the design please let me know and the price to do so.

Thanks.

***URGENT***

Marketing

```html
<!DOCTYPE html>
<html lang="en">
<head>
<meta charset="utf-8">
<title>Tindleport – February 2013 Newsletter</title>
<link rel="stylesheet" href="https://fonts.googleapis.com/css2?family=Ubuntu:ital,wght@0,400;0,500;0,700;1,500;1,700&family=Arimo:wght@400;700&display=swap">
<style>
:root{
  --ink:#3a3a3a;
  --dark:#2a2a2a;
  --header:#232323;
  --nav:#2c8cc5;
  --nav-line:#4aa2d6;
  --lime:#8cc63f;
  --lime-dark:#6ea52a;
  --panel:#eef8f9;
  --panel-line:#a9dde3;
  --red:#e8382c;
  --orange:#f47c14;
  --teal:#0e6f78;
  --olive:#5b6b12;
  --muted:#8a8a8a;
  --white:#ffffff;
}
*{box-sizing:border-box;margin:0;padding:0}
html,body{width:804px;height:1200px;overflow:hidden;background:var(--white)}
body{position:relative;font-family:"Ubuntu",sans-serif;color:var(--ink)}
.abs{position:absolute}

/* top strip */
.pre-header{left:0;top:0;width:804px;height:24px;background:var(--dark);font-family:"Arimo",sans-serif;font-size:9px;color:#b8b8b8;text-transform:uppercase;letter-spacing:.2px}
.pre-header .left{position:absolute;left:38px;top:8px}
.pre-header .left u{color:#d8d8d8}
.pre-header .right{position:absolute;right:41px;top:8px}

/* masthead */
.masthead{left:0;top:24px;width:804px;height:106px;background:repeating-linear-gradient(135deg,#272727 0 2px,#1f1f1f 2px 4px)}
.brand{left:42px;top:50px;display:flex;align-items:center;gap:10px}
.brand-dot{width:44px;height:44px;border-radius:50%;background:var(--lime)}
.brand-name{font-weight:700;font-size:30px;color:var(--lime);letter-spacing:1px}
.all-deals{left:609px;top:55px;width:151px;height:37px;border-radius:5px;background:linear-gradient(#9fd24b,var(--lime-dark));color:var(--white);font-weight:500;font-size:17px;text-align:center;line-height:37px}

/* navigation */
.nav{left:0;top:130px;width:804px;height:35px;background:var(--nav);display:flex}
.nav a{color:var(--white);text-decoration:none;font-weight:500;font-size:14px;line-height:35px;padding:0 12px 0 40px;border-right:1px solid var(--nav-line)}
.nav a+a{padding:0 14px 0 13px}
.nav a:nth-child(3){padding:0 14px 0 17px}
.issue-date{left:568px;top:133px;font-size:25px;font-weight:500;color:#2f3b44;letter-spacing:.5px}

/* featured deal */
.featured{left:38px;top:174px;width:721px;height:192px;background:var(--panel);border:1px solid var(--panel-line);border-radius:5px}
.featured-title{left:59px;top:187px;font-size:16.5px;font-weight:500;color:#333}
.featured-photo{left:58px;top:218px;width:207px;height:129px;border:3px solid #c9c9c9;background:linear-gradient(135deg,#b0a8a6,#e7dfe0 55%,#c74e5c)}
.featured-copy{left:277px;top:222px;width:196px;font-family:"Arimo",sans-serif;font-size:11.3px;line-height:19px;color:#4a4a4a}
.featured-price{left:509px;top:235px;font-size:30px;font-weight:500;color:var(--red)}
.hot{left:725px;top:170px;width:54px;height:54px;border-radius:50%;background:radial-gradient(circle at 40% 35%,#7ec34a,#3f9424);color:var(--white);font-weight:700;font-size:18px;text-align:center;line-height:54px;box-shadow:0 2px 3px rgba(0,0,0,.25)}

.deal-btn{display:block}
.deal-btn text{font-family:"Ubuntu",sans-serif;font-weight:700;fill:var(--white)}

.price-table{left:493px;top:281px;width:249px;height:72px;border:1px solid #cfcfcf;border-radius:3px;background:#e8e8e8;font-family:"Arimo",sans-serif}
.price-table .cells{display:flex;height:45px;border-bottom:1px solid #cfcfcf}
.price-table .cell{text-align:center;border-right:1px solid #d2d2d2;padding-top:6px}
.price-table .cell:last-child{border-right:0}
.price-table .label{font-size:8.5px;color:#444;text-transform:uppercase}
.price-table .value{font-size:13.5px;font-weight:700;margin-top:3px}
.value.struck{color:#777;text-decoration:line-through}
.value.hot-red{color:var(--red)}
.time-left{display:flex;align-items:center;height:26px;padding-left:24px;font-size:9px;color:#555;text-transform:uppercase}
.time-left b{color:var(--red);font-size:14px;margin-left:12px}
.time-left b small{font-size:9px;color:#333;margin-left:3px}
.time-left svg{margin-right:8px}

/* deals of the week */
.weekly{left:38px;top:378px;width:499px;height:720px;background:var(--panel);border:1px solid var(--panel-line);border-radius:4px;overflow:hidden}
.weekly-head{height:39px;background:linear-gradient(#f5911f,#ee6d0a);color:var(--white);font-style:italic;font-weight:700;font-size:22px;padding:4px 0 0 11px;text-shadow:0 1px 1px rgba(0,0,0,.25)}
.deal{position:absolute;left:0;width:497px}
.deal-photo{position:absolute;left:13px;width:179px;height:125px;border:1px solid #bdbdbd;background:linear-gradient(120deg,#f2f2f2,#e6e6e6 40%,#d9edf0)}
.deal-photo.framed{border:3px solid #c4c4c4}
.deal-name{position:absolute;left:215px;font-size:16.5px;font-weight:500;color:#444}
.deal-off{position:absolute;left:208px;font-size:16px;font-weight:500;color:var(--orange)}
.deal-exp{position:absolute;left:348px;font-size:11.5px;font-weight:500;color:var(--teal)}
.deal-exp sup{font-size:7px}
.deal-cost{position:absolute;left:225px;font-size:30px;font-weight:500;color:var(--olive)}
.deal-go{position:absolute;left:360px}
.rule{position:absolute;left:8px;width:474px;height:1px;background:#d4e7ea}

/* sidebar */
.sidebar{left:559px;top:378px;width:200px;height:720px;background:var(--panel);border:1px solid var(--panel-line);border-radius:4px}
.side-title{position:absolute;left:11px;font-style:italic;font-weight:700;font-size:16px;line-height:20px;color:var(--teal)}
.side-note{position:absolute;left:12px;top:58px;width:185px;font-family:"Arimo",sans-serif;font-size:11px;line-height:15px;color:#444}
.social{position:absolute;left:46px;top:102px;display:flex;gap:11px}
.social span{width:23px;height:23px;border-radius:50%;display:flex;align-items:center;justify-content:center}
.side-rule{position:absolute;left:8px;width:182px;height:1px;background:#d4e7ea}
.side-link{position:absolute;left:14px;width:170px;height:39px;border:1px solid #b9dfe3;border-radius:3px;background:#e1f1f3;font-style:italic;font-weight:700;font-size:14px;color:var(--orange);padding:10px 0 0 17px}
.cat-list{position:absolute;left:16px;list-style:none;font-family:"Arimo",sans-serif;font-size:11px;color:#333}
.cat-list li{height:20px;padding-left:13px;position:relative}
.cat-list li::before{content:"";position:absolute;left:0;top:4px;border-left:4px solid var(--teal);border-top:3px solid transparent;border-bottom:3px solid transparent}

/* footer */
.footer{left:0;top:1117px;width:804px;height:83px;background:var(--dark);font-family:"Arimo",sans-serif;text-align:center}
.footer-links{margin-top:19px;font-size:11px;color:var(--white);word-spacing:0}
.footer-links a{color:var(--white);text-decoration:none;margin:0 6px}
.footer-note{margin-top:10px;font-size:10.5px;line-height:13px;color:#a6a6a6}
.footer-note .addr{color:#a8651d}
</style>
</head>
<body>

<div class="abs pre-header">
  <div class="left"><u>Click here</u> if this email does not display correctly</div>
  <div class="right">Sign in | Sign up | Contact us | Help videos</div>
</div>

<header class="abs masthead"></header>
<div class="abs brand"><span class="brand-dot"></span><span class="brand-name">TINDLEPORT</span></div>
<div class="abs all-deals">VIEW ALL DEALS</div>

<nav class="abs nav">
  <a href="#">DISCOUNT DEALS</a>
  <a href="#">FREE INCENTIVES</a>
  <a href="#">MARKETPLACE ITEMS</a>
</nav>
<div class="abs issue-date">FEBRUARY 2013</div>

<!-- featured deal -->
<section class="abs featured"></section>
<h2 class="abs featured-title">Vintage Gift Set for Two ($24), Three ($36) or Four People ($48)...</h2>
<div class="abs featured-photo" role="img" aria-label="Product photo of a colourful vintage gift set of painted wooden figures"></div>
<p class="abs featured-copy">Lorem ipsum dolor sit amet conse ctetur adipisicing elit, sed do eiusmod tempor incididunt ut labore et dolore magna aliqua. Ut enim ad minim veniam, quis nostrud exercitation ullamco laboris nisi ut aliquip ex ea</p>
<div class="abs featured-price">$24</div>
<svg class="abs deal-btn" style="left:604px;top:236px" width="126" height="34" viewBox="0 0 126 34">
  <defs><linearGradient id="btnRed" x1="0" y1="0" x2="0" y2="1"><stop offset="0" stop-color="#ff5a3c"/><stop offset="1" stop-color="#de2718"/></linearGradient></defs>
  <path d="M3 0H110L124 16 110 32H3a3 3 0 0 1-3-3V3a3 3 0 0 1 3-3z" fill="url(#btnRed)"/>
  <circle cx="113" cy="16" r="2.4" fill="#fff"/>
  <text x="56" y="22" font-size="16" text-anchor="middle">VIEW DEAL</text>
</svg>
<div class="abs hot">HOT</div>

<div class="abs price-table">
  <div class="cells">
    <div class="cell" style="width:75px"><div class="label">Full price</div><div class="value struck">$125</div></div>
    <div class="cell" style="width:98px"><div class="label">Full price</div><div class="value hot-red">30%</div></div>
    <div class="cell" style="width:74px"><div class="label">Save</div><div class="value hot-red">$38.5</div></div>
  </div>
  <div class="time-left">
    <svg width="18" height="18" viewBox="0 0 18 18"><rect x="0.5" y="0.5" width="17" height="17" rx="3" fill="#fff" stroke="#999"/><circle cx="9" cy="9" r="6" fill="none" stroke="#777" stroke-width="1.4"/><path d="M9 5v4h3" stroke="#555" stroke-width="1.4" fill="none"/></svg>
    Time left <b>3<small>D</small></b><b>2<small>HRS</small></b><b>20<small>Min</small></b>
  </div>
</div>

<!-- deals of the week -->
<section class="abs weekly">
  <h2 class="weekly-head">Deals of the Week</h2>

  <article class="deal" style="top:0">
    <div class="deal-photo" style="top:54px" role="img" aria-label="Product photo of coloured charging cables and adapters"></div>
    <h3 class="deal-name" style="top:62px">Vintage Gift Set for Two ($24)</h3>
    <span class="deal-off" style="top:91px">30% off Purchase</span>
    <span class="deal-exp" style="top:95px">Expires Feb 10<sup>th</sup>,2013</span>
    <span class="deal-cost" style="top:126px">$250</span>
    <svg class="deal-go" style="top:133px" width="100" height="26" viewBox="0 0 100 26"><path d="M3 0H86L97 12 86 24H3a3 3 0 0 1-3-3V3a3 3 0 0 1 3-3z" fill="url(#btnRed)"/><circle cx="88" cy="12" r="2" fill="#fff"/><text class="" x="45" y="17" font-size="12" text-anchor="middle" font-family="Ubuntu,sans-serif" font-weight="700" fill="#fff">VIEW DEAL</text></svg>
  </article>
  <div class="rule" style="top:191px"></div>

  <article class="deal" style="top:160px">
    <div class="deal-photo" style="top:54px" role="img" aria-label="Product photo of coloured charging cables and adapters"></div>
    <h3 class="deal-name" style="top:62px">Vintage Gift Set for Two ($24)</h3>
    <span class="deal-off" style="top:91px">30% off Purchase</span>
    <span class="deal-exp" style="top:95px">Expires Feb 10<sup>th</sup>,2013</span>
    <span class="deal-cost" style="top:126px">$250</span>
    <svg class="deal-go" style="top:133px" width="100" height="26" viewBox="0 0 100 26"><path d="M3 0H86L97 12 86 24H3a3 3 0 0 1-3-3V3a3 3 0 0 1 3-3z" fill="url(#btnRed)"/><circle cx="88" cy="12" r="2" fill="#fff"/><text x="45" y="17" font-size="12" text-anchor="middle" font-family="Ubuntu,sans-serif" font-weight="700" fill="#fff">VIEW DEAL</text></svg>
  </article>
  <div class="rule" style="top:357px"></div>

  <article class="deal" style="top:321px">
    <div class="deal-photo" style="top:54px" role="img" aria-label="Product photo of coloured charging cables and adapters"></div>
    <h3 class="deal-name" style="top:62px">Vintage Gift Set for Two ($24)</h3>
    <span class="deal-off" style="top:91px">30% off Purchase</span>
    <span class="deal-exp" style="top:95px">Expires Feb 10<sup>th</sup>,2013</span>
    <span class="deal-cost" style="top:126px">$250</span>
    <svg class="deal-go" style="top:133px" width="100" height="26" viewBox="0 0 100 26"><path d="M3 0H86L97 12 86 24H3a3 3 0 0 1-3-3V3a3 3 0 0 1 3-3z" fill="url(#btnRed)"/><circle cx="88" cy="12" r="2" fill="#fff"/><text x="45" y="17" font-size="12" text-anchor="middle" font-family="Ubuntu,sans-serif" font-weight="700" fill="#fff">VIEW DEAL</text></svg>
  </article>
  <div class="rule" style="top:518px"></div>

  <article class="deal" style="top:497px">
    <div class="deal-photo framed" style="top:54px" role="img" aria-label="Product photo of coloured charging cables and adapters"></div>
    <h3 class="deal-name" style="top:62px">Vintage Gift Set for Two ($24)</h3>
    <span class="deal-off" style="top:91px">30% off Purchase</span>
    <span class="deal-exp" style="top:95px">Expires Feb 10<sup>th</sup>,2013</span>
    <span class="deal-cost" style="top:126px">$250</span>
    <svg class="deal-go" style="top:133px" width="100" height="26" viewBox="0 0 100 26"><path d="M3 0H86L97 12 86 24H3a3 3 0 0 1-3-3V3a3 3 0 0 1 3-3z" fill="url(#btnRed)"/><circle cx="88" cy="12" r="2" fill="#fff"/><text x="45" y="17" font-size="12" text-anchor="middle" font-family="Ubuntu,sans-serif" font-weight="700" fill="#fff">VIEW DEAL</text></svg>
  </article>
  <div class="rule" style="top:694px"></div>
</section>

<!-- sidebar -->
<aside class="abs sidebar">
  <h3 class="side-title" style="top:12px">Join our<br>Community</h3>
  <svg style="position:absolute;left:152px;top:18px" width="24" height="26" viewBox="0 0 24 26"><path d="M7 11l5-9c2 0 3 1 2.5 3.5L13.5 10H21a2 2 0 0 1 1.6 3l-3 9a2 2 0 0 1-2 1.5H7z" fill="#f2c23a" stroke="#b98a16"/><rect x="1" y="11" width="6" height="13" rx="1" fill="#9bb7c9" stroke="#6d8797"/></svg>
  <p class="side-note">Follow us for Shopping exclusive &amp; Daily deals</p>
  <div class="social">
    <span style="background:#3b5ca0"></span>
    <span style="background:#35b6e8"></span>
    <span style="background:#8cc63f"><svg width="13" height="10" viewBox="0 0 13 10"><rect x="0.6" y="0.6" width="11.8" height="8.8" rx="1" fill="none" stroke="#fff" stroke-width="1.2"/><path d="M1 1l5.5 4.5L12 1" fill="none" stroke="#fff" stroke-width="1.2"/></svg></span>
  </div>
  <div class="side-rule" style="top:137px"></div>

  <div class="side-link" style="top:151px">NEW COUPONS</div>
  <div class="side-link" style="top:201px">EXCLUSIVES</div>
  <div class="side-link" style="top:249px">MOST POPULAR</div>
  <div class="side-link" style="top:298px">EXPIRING SOON</div>
  <div class="side-rule" style="top:357px"></div>

  <h3 class="side-title" style="top:372px">Popular<br>This week</h3>
  <svg style="position:absolute;left:159px;top:374px" width="26" height="32" viewBox="0 0 26 32"><path d="M7 18l-3 13 5-3 3 4 2-12zM19 18l3 13-5-3-3 4-2-12z" fill="#2a8f87"/><circle cx="13" cy="12" r="11" fill="#39b0a6" stroke="#1f7b74"/><circle cx="13" cy="12" r="6" fill="none" stroke="#d9f3f0" stroke-width="1.5"/></svg>
  <ul class="cat-list" style="top:422px">
    <li>Electronics</li><li>Clothing &amp; Shoes</li><li>Health &amp; Beauty</li><li>Tous &amp; Hobby</li><li>Home &amp; Kitchen</li>
  </ul>
  <div class="side-rule" style="top:527px"></div>

  <h3 class="side-title" style="top:544px">Seasonal<br>Coupons</h3>
  <svg style="position:absolute;left:161px;top:537px" width="24" height="22" viewBox="0 0 24 22"><rect x="1" y="2" width="22" height="19" rx="1.5" fill="#fff" stroke="#888"/><rect x="1" y="2" width="22" height="5" fill="#d8443a"/><path d="M5 10h14M5 13h14M5 16h14M9 8v11M13 8v11M17 8v11" stroke="#aaa" stroke-width=".8"/></svg>
  <ul class="cat-list" style="top:594px">
    <li>Electronics</li><li>Clothing &amp; Shoes</li><li>Health &amp; Beauty</li><li>Tous &amp; Hobby</li><li>Home &amp; Kitchen</li>
  </ul>
</aside>

<footer class="abs footer">
  <div class="footer-links"><a href="#">About</a> <a href="#">Help</a> <a href="#">Contact Us</a> &nbsp; <a href="#">Terms Privacy</a></div>
  <p class="footer-note">You received this email because you are registered on tindleport.com with the email address: <span class="addr">jane.doe@mailbox.test</span>.<br>You can change your email settings or click here to unsubscribe.</p>
</footer>

</body>
</html>
```